Brochure for Specialist Divorce Support

1. I want an A4 three fold brochure or DL to promote my business and services.
My market are people going through divorce and are usually feeling very overwhelmed and therefore not functioning very well - both men and women, age early forties,
2. Colours – variety of blues and lime greens but you choose if you need a contrast e.g. orange
3. Images – happy single families
4. Theme - could you make it around water please - soothing
5. Logos – HWN &; HWT (I will attach)
6. I have a lot of content so maybe not too busy but still professional feel +
warm and reassuring
7. I'm attaching -

- a draft brochure I put together using a Microsoft template
- a word document with extra details
- plus two logos to do with my qualifications
- and some images for you to choose from

7. I want to use this as a template for some other brochures -> more work for
the winner.

Target Market(s)

Men and women usually in their early forties with primary school aged children i.e 5 to 12 years old.
They are going through a divorce and very upset, Maybe losing contact with their children and their way of life as they know it is disappearing. They are in turmoil and not functioning as well as they usually do.

Industry/Entity Type

Business

Font styles to use
Sans Serif

Colors
34a7d7
abd037
3277b5

Requirements
Must have
• I want the brochure to be three folds with the center the full A4
• Could you make the theme around water please.
• I will upload some photos for you to use if you want,

```html
<!DOCTYPE html>
<html lang="en">
<head>
<meta charset="utf-8">
<title>Specialist Divorce Support – Tri-fold Brochure</title>
<link rel="stylesheet" href="https://fonts.googleapis.com/css2?family=Open+Sans:ital,wght@0,400;0,600;0,700;1,400;1,600&display=swap">
<style>
:root{
  --sky:#34a7d7;
  --lime:#abd037;
  --ocean:#3277b5;
  --navy:#2a5f9a;
  --ink:#4a4a4a;
  --pale:#e3f1f9;
  --paper:#ffffff;
  --bg:#5d5d5d;
}
*{box-sizing:border-box;margin:0;padding:0}
html,body{width:952px;height:1200px;overflow:hidden}
body{background:var(--bg);font-family:"Open Sans",sans-serif;color:var(--ink);position:relative}
.spread{position:absolute;left:16px;width:920px;height:575px;display:flex;background:var(--paper);overflow:hidden}
.spread.outside{top:16px}
.spread.inside{top:609px}
.panel{position:relative;width:306.67px;height:100%;overflow:hidden}
.panel + .panel{border-left:1px solid #cfd8df}
.panel-content{position:absolute;z-index:4}
.photo{position:absolute}
.tint-pale{background:linear-gradient(180deg,#cfe6f4 0%,#eef6fb 60%,#ffffff 100%)}
h3.lead{color:var(--ocean);font-size:12.5px;font-weight:700}
.bullets{list-style:none}
.bullets li{position:relative;padding-left:9px;font-size:10px;line-height:1.2;text-align:justify;margin-bottom:5px}
.bullets li::before{content:"";position:absolute;left:0;top:4px;width:5px;height:5px;border-radius:50%;background:var(--lime)}
.bullets.tight li{margin-bottom:1px;line-height:1.17}
.note{font-style:italic;text-align:center;font-size:11px;line-height:1.3}
.urlbox{position:absolute;bottom:0;height:32px;background:#fff;color:#444;font-weight:600;font-size:11px;display:flex;align-items:center;justify-content:center;border-radius:3px 3px 0 0}
.brand{font-weight:700;font-size:15px;color:var(--ocean);display:inline-flex;align-items:center;gap:5px}
.brand .dot{width:10px;height:10px;border-radius:50%;background:var(--lime)}
.stage{position:relative;padding-left:20px;margin-bottom:6px}
.stage .num{position:absolute;left:0;top:-4px;font-size:28px;font-weight:400;color:var(--lime);line-height:1}
.stage h4{color:var(--sky);font-size:11px;font-weight:700}
.stage .sub{color:var(--sky);font-style:italic;font-size:10.5px}
.body{font-size:10px;line-height:1.18;text-align:justify}
.quote{font-size:10px;font-style:italic;text-align:justify;line-height:1.3;color:#555}
.quote .mark{color:var(--lime);font-weight:700;font-size:15px;font-style:normal;margin-right:4px}
</style>
</head>
<body>

<section class="spread outside">
  <div class="panel tint-pale">
    <div class="panel-content" style="left:14px;top:20px;right:14px">
      <h3 class="lead" style="margin-bottom:8px">Coaching can help you:</h3>
      <ul class="bullets">
        <li>Save money by being a more collected and credible client in the legal process</li>
        <li>Stay in control and focus on what's important for you and your family to avoid angry, emotional hijacks</li>
        <li>Feel more empowered by being organised and prepared for what's ahead and develop a plan of action</li>
        <li>Identify your next steps re: legal, financial, children's issues plus your self-care</li>
        <li>Develop a draft parenting plan to anticipate and address possible issues pertinent to your family</li>
        <li>Consider areas of possible conflict and explore techniques to reduce confrontation</li>
        <li>Find your voice and be more confident in your skills to take control of your divorce and do it your way</li>
        <li>Let go of what was … and create what is possible during your divorce journey and afterwards</li>
      </ul>
      <p class="note" style="color:var(--ocean);margin-top:6px">Coaching works well over the phone, allowing for flexibility of time and place - evening appointments available.</p>
    </div>
    <div class="photo" role="img" aria-label="Mother and two children standing at the water's edge on a beach" style="left:0;right:0;top:365px;bottom:0;background:linear-gradient(180deg,rgba(238,246,251,0) 0%,#7fc6e4 22%,#2fa3cf 50%,#8ed1e6 68%,#e9dcc5 85%,#dccdb2 100%)"></div>
  </div>

  <div class="panel" style="background:#fff">
    <div class="photo" role="img" aria-label="Father hugging his young son, circular photo" style="left:58px;top:8px;width:168px;height:168px;border-radius:50%;border:5px solid #cfe6f4;background:radial-gradient(circle at 50% 40%,#f3f7fa 0%,#c6d6e2 45%,#7e98ae 100%)"></div>
    <div class="panel-content" style="left:14px;right:14px;top:186px">
      <h3 style="color:var(--ocean);font-size:12px;font-weight:700;text-align:center;margin-bottom:12px">SERVICES</h3>
      <ul class="bullets">
        <li>Specialist divorce support to suit your needs</li>
        <li>Pre-mediation coaching helping you prepare and achieve more positive outcomes to avoid going to court</li>
        <li>Collaborative law coaching to increase crucial skills so you can participate more constructively in negotiations</li>
        <li>Delivery of HWN Conflict Profile giving you real feedback on the constructive and destructive behaviours you choose during conflict situations to facilitate more productive discussions</li>
        <li>Corporate Conflict Management Training</li>
      </ul>
      <div style="display:flex;justify-content:center;gap:26px;margin-top:12px">
        <span class="brand" style="color:#c0392b"><span class="dot"></span>HWN</span>
        <span class="brand"><span class="dot"></span>HWT</span>
      </div>
    </div>
    <svg style="position:absolute;left:0;top:395px" width="307" height="180" viewBox="0 0 307 180" aria-hidden="true">
      <path d="M0 20 C60 70 180 70 307 10 L307 180 L0 180 Z" fill="var(--lime)"/>
      <path d="M0 40 C70 80 190 80 307 24 L307 180 L0 180 Z" fill="#fff"/>
      <path d="M0 58 C80 90 200 88 307 38 L307 180 L0 180 Z" fill="var(--ocean)"/>
    </svg>
    <div class="panel-content" style="left:0;right:0;top:480px;text-align:center;color:#fff;font-size:7px;line-height:1.45;font-weight:600">
      <div style="font-size:8px;font-weight:700">MEREDITH ………….</div>
      <div>HWT Certified Divorce Coach</div>
      <div>Tideline Trained Conflict Coach</div>
      <div>Cert IV in Training &amp; Assessment</div>
      <div>Accredited in HWN Conflict Profile</div>
      <div>BA (Ind. Relations) (Brisbane)</div>
    </div>
    <div class="urlbox" style="left:24px;width:255px">www.harbourwaycoaching.com.au</div>
  </div>

  <div class="panel" style="background:var(--ocean)">
    <div class="photo" role="img" aria-label="Smiling mother hugging her daughter outdoors" style="left:0;right:0;top:0;height:440px;background:linear-gradient(135deg,#c8d48a 0%,#e8c9a6 35%,#d8a98a 55%,#9fb3c8 80%,#6c8fb8 100%)"></div>
    <div class="panel-content" style="right:14px;top:12px"><span class="brand" style="color:#fff"><span class="dot" style="background:#fff"></span>HWT</span></div>
    <svg style="position:absolute;left:0;top:360px" width="307" height="120" viewBox="0 0 307 120" aria-hidden="true">
      <path d="M0 120 L0 80 C90 90 200 60 307 0 L307 120 Z" fill="var(--lime)"/>
      <path d="M0 120 L0 92 C100 98 210 72 307 22 L307 120 Z" fill="var(--ocean)"/>
    </svg>
    <h2 class="panel-content" style="left:0;right:0;top:444px;text-align:center;color:#fff;font-size:15px;font-weight:700">SPECIALIST DIVORCE SUPPORT</h2>
    <p class="note panel-content" style="left:10px;right:10px;top:474px;color:#e5f2fb;font-size:15px;line-height:1.22">Helping you move through this major life challenge so you can more successfully start living your new life – your way!</p>
    <div class="urlbox" style="left:24px;width:255px">www.harbourwaycoaching.com.au</div>
  </div>
</section>

<section class="spread inside">
  <div class="photo" role="img" aria-label="Mother walking with her two sons along the shoreline" style="left:0;top:0;width:614px;height:200px;background:linear-gradient(180deg,#d9e9f3 0%,#b9d7ea 40%,#5a9ec9 62%,#a7c9dc 78%,#d7dcdc 100%);z-index:1"></div>
  <svg style="position:absolute;left:0;top:150px;z-index:2" width="614" height="80" viewBox="0 0 614 80" aria-hidden="true">
    <path d="M0 40 C160 10 420 60 614 0 L614 80 L0 80 Z" fill="var(--lime)"/>
    <path d="M0 56 C170 26 430 74 614 14 L614 80 L0 80 Z" fill="#fff"/>
  </svg>
  <p class="note" style="position:absolute;left:10px;top:32px;width:300px;z-index:3;color:var(--navy);font-weight:600;font-size:13px;line-height:1.22">Together we will identify your goals, set priorities and develop a plan for tomorrow … moving you through the pain of divorce to regain confidence and start anew.</p>

  <div class="panel" style="background:linear-gradient(180deg,#fff 40%,#eef6fb 100%)">
    <div class="panel-content" style="left:14px;right:14px;top:236px">
      <h3 class="lead" style="margin-bottom:9px">You will go through distinct stages:</h3>
      <div class="stage"><span class="num">1</span><h4>THE PREPARATION STAGE</h4><div class="sub">maybe entail one or two coaching sessions</div></div>
      <p class="body" style="margin-bottom:8px">Anticipating all the unknowns and preparing before you see a Family Law Solicitor can save a lot of your solicitor's time and therefore money. The clearer you are on what you want to achieve throughout the process, the more specific legal advice you will receive.</p>
      <div class="stage"><span class="num">2</span><h4>THE BUSINESS SIDE OF DIVORCE</h4><div class="sub">maybe two to four coaching sessions</div></div>
      <p class="body">Divorce involves multiple areas of change, intensity of emotions, life changing decisions, loss of family structure and often a sense of isolation not experienced before. Necessary<br>The emotional overwhelm associated with relationship breakdown and the associated loss of 24/7 contact with children can impact even the most together person's ability to make well considered decisions.<br>Together, we will process emotions constructively and clarify decisions to be made… for you to be better able to communicate these in negotiations as well as set new boundaries.</p>
    </div>
  </div>

  <div class="panel" style="background:#fff">
    <div class="panel-content" style="left:14px;right:14px;top:250px">
      <p style="color:#8fb52a;font-style:italic;font-size:10.5px;line-height:1.3;margin-bottom:7px">Where necessary we can work on skills you will need for successful outcomes with property settlements and parenting orders e.g.</p>
      <ul class="bullets tight">
        <li>Conflict resolution skills plus specific verbal &amp; written communication skills important for more neutral emails and messages</li>
        <li>Having difficult conversations</li>
        <li>Preparing before attending joint conferences or mediation</li>
        <li>Managing anger</li>
        <li>Supporting your children to also navigate changed family structures</li>
        <li>Strategies for you to start healing and become whole again</li>
        <li>Drafting a parenting plan to anticipate &amp; address possible parenting issues, leading to more positive and successful co-parenting in the long term. This is in everyone's interests… especially your children's</li>
        <li>Grieving losses … even if you are the one who made the decision to leave</li>
        <li>Look at possible stress strategies to sustain your energy levels, important for you to make good considered decisions</li>
      </ul>
    </div>
  </div>

  <div class="panel" style="background:#cfe8f6">
    <div class="photo" role="img" aria-label="Calm sea at sunset with soft golden light" style="left:0;right:0;top:370px;bottom:0;background:linear-gradient(180deg,#cfe8f6 0%,#b7c9d3 18%,#a59c94 40%,#c9a67e 62%,#8a7d73 82%,#5e6468 100%)"></div>
    <div class="panel-content" style="left:12px;right:14px;top:18px">
      <div class="stage"><span class="num">3</span><h4 style="color:var(--ocean)">THE MOVING ON STAGE</h4><div class="sub" style="color:var(--ocean)">one or two coaching sessions</div></div>
      <p class="body" style="margin:-2px 0 8px">Dealing with endings and focusing on the future:</p>
      <ul class="bullets">
        <li style="margin-bottom:3px">Changing your "self" image and building self worth</li>
        <li style="margin-bottom:3px">Transitioning from married life to being single again</li>
        <li style="margin-bottom:3px">Address barriers preventing you form moving forward</li>
        <li style="margin-bottom:3px">Setting realistic goals to help transition to your new life more effectively</li>
      </ul>
      <p class="note" style="color:#8fb52a;margin:12px 0 18px">Everyone is different and moves through the stages at their own pace.</p>
      <p class="quote" style="margin-bottom:14px"><span class="mark">“</span>Often family and friends can try to influence decisions based on what they see as best, so you can feel under an enormous pressure to keep them happy. Coaching offers an objective and neutral sounding board there just for you."</p>
      <p class="quote"><span class="mark">“</span>Even the most together person can be totally unprepared for the emotional overwhelm that divorce can bring, regardless if they are the one who made the decision to leave."</p>
    </div>
    <div class="panel-content" style="left:12px;right:14px;top:380px;color:#fff">
      <h4 style="text-align:center;font-style:italic;font-size:11px;font-weight:600;margin-bottom:6px">Testimonial</h4>
      <p class="quote" style="color:#fff;font-size:9.6px;line-height:1.2;margin-bottom:10px"><span class="mark">“</span>After many cups of coffee and long hours of listening to me, my very good friend suggested I speak to Meredith, a divorce coach. I was a bit sceptical, especially when a phone session was suggested. From my first phone session I felt empowered. It gave me a sense of direction, assisted me to set realistic goals and action plans. Most importantly it aided my self esteem.</p>
      <p class="quote" style="color:#fff;font-size:9.6px;line-height:1.2;margin-bottom:10px">Divorce is overwhelming. Talking to a caring professional like Meredith helped me acknowledge my priorities and a way to achieve them. Thank you Meredith."</p>
      <p style="font-size:10px">Lucinda - Brisbane, QLD</p>
    </div>
  </div>
</section>

</body>
</html>
```